Business card and letterhead for homeowners insurance company
Birchwell Insurance
Simple
Marissa Colvendra
Chief Financial Officer
418 Tolland Avenue Suite C Bradenton, Florida 34205
mcolvendra@birchwellhome.com
www.birchwellhome.com
Considering the following phrase centered on the back of the card. Please use fonts that mimic what would be displayed in a dictionary, as this is the literal definition of an "anchor". birch-well (noun) - a person or thing that can be relied on for support, security or stability.
marvetholdin marvetholdin
These look great! Anyway we can incorporate a little green in the design? Would love to see this green: #8dc73f. We will be using this on the website too. But it should be a very little pop of color (maybe replacing some of the gray I'm seeing). Wow!!

```html
<!DOCTYPE html>
<html lang="en">
<head>
<meta charset="utf-8">
<title>Birchwell Insurance – Business Card</title>
<link rel="stylesheet" href="https://fonts.googleapis.com/css2?family=Libre+Baskerville:ital,wght@0,400;0,700;1,400&family=Montserrat:wght@300;400&display=swap">
<style>
  :root{
    --navy:#2b3a78;
    --navy-deep:#1f2b5e;
    --paper:#ffffff;
    --ink:#3a3f52;
    --rule:#8a8fa3;
    --leaf:#8dc73f;
    --stage:#e7e8ec;
  }
  *{margin:0;padding:0;box-sizing:border-box}
  html,body{width:1200px;height:901px;overflow:hidden}
  body{background:var(--stage);position:relative;font-family:"Libre Baskerville",Georgia,serif}

  .card{position:absolute;width:620px;height:354px;border-radius:14px;overflow:hidden;
        box-shadow:0 6px 18px rgba(20,25,50,.18)}

  /* back of card */
  .card--back{left:290px;top:60px;background:var(--navy)}
  .back-mark{position:absolute;left:0;right:0;top:96px;
        display:flex;flex-direction:column;align-items:center;gap:14px}
  .back-mark__dot{width:22px;height:22px;border-radius:50%;background:var(--paper)}
  .back-mark__name{color:var(--paper);font-size:26px;letter-spacing:3px;text-transform:uppercase;
        white-space:nowrap;text-align:center}
  .definition{position:absolute;left:60px;right:60px;bottom:64px;text-align:center;
        color:var(--paper);font-size:14px;line-height:1.6}
  .definition__word{font-weight:700}
  .definition__pos{font-style:italic}

  /* front of card */
  .card--front{left:290px;top:487px;background:var(--paper)}
  .brand{position:absolute;left:34px;top:118px;width:250px;display:flex;align-items:center;gap:12px}
  .brand__dot{width:16px;height:16px;border-radius:50%;background:var(--navy);flex:none}
  .brand__name{color:var(--navy);font-size:21px;letter-spacing:2px;text-transform:uppercase;line-height:1.25}
  .divider{position:absolute;left:300px;top:62px;width:1px;height:186px;background:var(--rule)}
  .contact{position:absolute;left:326px;top:62px;color:var(--ink);font-size:12px;line-height:1.5;font-style:normal}
  .contact__name{color:var(--navy);font-weight:700;font-size:15px}
  .contact__title{font-style:italic;font-size:12px;margin-bottom:14px}
  .contact__address{margin-bottom:12px}
  .footer-band{position:absolute;left:0;bottom:0;width:620px;height:60px}
  .footer-url{position:absolute;right:30px;bottom:10px;color:var(--paper);
        font-family:"Montserrat",Arial,sans-serif;font-size:13px;letter-spacing:1.5px}
</style>
</head>
<body>

<section class="card card--back" aria-label="Back of business card">
  <div class="back-mark">
    <span class="back-mark__dot"></span>
    <span class="back-mark__name">Birchwell Insurance</span>
  </div>
  <p class="definition">
    <span class="definition__word">birch·well</span> <span class="definition__pos">(noun)</span> – a shelter or partner that can be relied on for support, security or stability.
  </p>
</section>

<section class="card card--front" aria-label="Front of business card">
  <div class="brand">
    <span class="brand__dot"></span>
    <span class="brand__name">Birchwell Insurance</span>
  </div>

  <div class="divider"></div>

  <address class="contact">
    <div class="contact__name">Marissa Colvendra</div>
    <div class="contact__title">Chief Financial Officer</div>
    <div class="contact__address">418 Tolland Avenue<br>Suite C<br>Bradenton, Florida 34205</div>
    <div>P: 941.555.0142</div>
    <div>C: 941.555.0187</div>
    <div>E: mcolvendra@birchwellhome.com</div>
  </address>

  <svg class="footer-band" viewBox="0 0 620 60" aria-hidden="true">
    <line x1="0" y1="14" x2="620" y2="14" stroke="var(--navy)" stroke-width="2"/>
    <line x1="0" y1="20" x2="620" y2="20" stroke="var(--leaf)" stroke-width="2"/>
    <polygon points="230,26 620,26 620,60 204,60" fill="var(--navy)"/>
    <polygon points="212,26 222,26 196,60 186,60" fill="var(--navy)"/>
    <polygon points="196,26 204,26 178,60 170,60" fill="var(--navy-deep)"/>
  </svg>
  <span class="footer-url">www.birchwellhome.com</span>
</section>

</body>
</html>
```